Modern design for a Septic Tank maintenance company

Task Description
- The design should be based around the attached HPID (home page information design) called Koru Flow Septic Services HPID. The table boxes are just for approximate placement of information – you DON'T have to make it look exactly like this.
- Information only is in orange text. Copy to go on the design in black text. Some instructions are in the HPID. Please be creative! You don’t have to use the exact images provided if you have a better idea.

- The design needs to be clean and spacious. Please use the colours from the logos in the website design. LOTS of white too. Don't need to use all the images attached some are customer supplied and might only be good for the smaller images.

I've attached home page gallery example photo called Tarewa beach. You can use this or something similar - be creative please!

Width of content will be 1100 pixels when implemented as a web page. Header height (without nav bar) 150-160 pixels.

The winning PSD file will have to be provided as follows…
1. Canvas size of 2000px x 2000px - 72ppi in Adobe Photoshop (CS5 compatible)
2. Width of content section is 1100px wide - centered in the canvas
3. Any button rollovers/hovers in the PSD as hidden layers.
4. All fonts used must be Google fonts (except for the fonts in the header at the top of the page).
5. You will need to supply the chosen home page plus one example page (example page as a style guide for how all other pages will look). Example page is only the header and navigational bar at the top, an empty sector in the middle with a column (180 px wide) which can be left or right aligned which means the main sector is 920 pixels wide, and then the footer at the bottom of the page.

Industry/Entity Type

It Company

```html
<!DOCTYPE html>
<html lang="en">
<head>
<meta charset="utf-8">
<title>Koru Flow Septic Services</title>
<link rel="stylesheet" href="https://fonts.googleapis.com/css2?family=Roboto:ital,wght@0,300;0,400;0,500;0,700;1,400&family=Roboto+Condensed:wght@700&display=swap">
<style>
:root{
  --teal:#1dbb94;
  --teal-dark:#17977a;
  --ink:#2b2b2b;
  --body:#444;
  --nav:#1b1b1b;
  --footer:#262626;
  --footer-base:#1f1f1f;
  --panel:#e9e9e9;
  --white:#fff;
}
*{box-sizing:border-box;margin:0;padding:0}
html,body{width:1028px;height:1200px;overflow:hidden;background:var(--white)}
body{position:relative;font-family:"Roboto",Arial,sans-serif;color:var(--ink)}
.abs{position:absolute}
.top-rule{left:0;top:0;width:1028px;height:3px;background:var(--teal)}

/* header */
.brand{left:198px;top:30px;display:flex;align-items:center;gap:10px}
.brand-dot{width:40px;height:40px;border-radius:50%;background:var(--teal)}
.brand-name{font-size:22px;font-weight:500;color:var(--ink);line-height:1.1;width:220px}
.divider{width:1px;height:48px;background:#cfcfcf;top:28px}
.tagline{left:494px;top:28px;width:180px;font-size:10.5px;line-height:12px;color:#333}
.service-area{right:201px;top:27px;text-align:right;font-size:8.5px;line-height:10px;color:#333;width:150px}
.phone-icon{left:693px;top:53px}
.phones{left:723px;top:52px;font-size:11px;font-weight:700;line-height:13px;color:#111}

/* nav */
.main-nav{left:196px;top:102px;width:636px;height:30px;background:var(--nav);border-radius:4px 4px 0 0}
.main-nav a{position:absolute;top:9px;font-size:10.5px;color:var(--white);text-decoration:none;text-transform:uppercase;white-space:nowrap}
.main-nav a.is-active{color:var(--teal)}

/* hero */
.hero{left:196px;top:131px;width:636px;height:258px;border-radius:0 0 6px 6px;overflow:hidden;
  background:linear-gradient(180deg,#a9c8e6 0%,#6f9ec2 25%,#2f5232 42%,#1c3b5f 60%,#3a78b4 72%,#a7c4d6 85%,#7f8a52 100%)}
.hero-callout{left:586px;top:138px;width:230px}
.hero-callout h1{position:absolute;top:4px;left:12px;width:206px;text-align:center;font-size:23.5px;font-weight:300;line-height:23px;color:#333}
.hero-callout p{position:absolute;top:82px;left:10px;width:210px;text-align:center;font-size:9.5px;font-style:italic;line-height:12.5px;color:#333}
.slider-dots{left:475px;top:380px;width:80px;height:14px;background:var(--white);border-radius:8px 8px 0 0}
.slider-dots span{position:absolute;top:4px;width:5px;height:5px;border-radius:50%;background:#c8c8c8}
.slider-dots span.is-current{background:#555}

/* intro */
.intro-title{left:0;top:407px;width:1036px;text-align:center;font-family:"Roboto Condensed",Arial,sans-serif;font-weight:700;font-size:22.5px;letter-spacing:-.3px;color:var(--ink);white-space:nowrap}
.intro-sub{left:0;top:435px;width:1036px;text-align:center;font-size:12.5px;color:#222}
.intro-shadow{left:215px;top:458px;width:605px;height:8px;border-radius:50%;box-shadow:0 5px 6px -3px rgba(0,0,0,.12)}

/* features */
.feature h2{position:absolute;left:8px;top:0;width:195px;font-size:13px;font-weight:500;line-height:16px;color:#222}
.feature .photo{position:absolute;top:37px;width:197px;height:84px;border-radius:4px;border:1px solid #777}
.feature p{position:absolute;top:126px;font-size:9.2px;line-height:12px;color:var(--body);letter-spacing:.1px}
.feature p a{color:#222;font-weight:700;text-decoration:underline}
.btn{position:absolute;height:21px;width:77px;background:var(--teal);border-radius:3px;color:var(--white);font-size:9.5px;font-weight:700;text-align:center;line-height:21px;text-transform:uppercase}
.note{left:198px;top:766px;font-size:8.5px;color:#222}
.note b{font-weight:700}

/* enquiry */
.enquiry{left:195px;top:801px;width:637px;height:105px;background:var(--panel);border-radius:3px}
.enquiry-lead{left:195px;top:801px}
.enquiry-lead h3{position:absolute;left:14px;top:22px;font-size:16px;font-weight:400;color:var(--white);white-space:nowrap}
.enquiry-lead p{position:absolute;left:14px;top:46px;width:150px;font-size:10.5px;line-height:16px;color:var(--white)}
.field{position:absolute;background:var(--white);font-size:9px;color:#666;padding:4px 6px}
.send{left:768px;top:882px;width:54px;height:18px;background:var(--teal-dark);color:var(--white);font-size:9px;font-weight:700;text-align:center;line-height:18px}

/* footer */
.site-footer{left:0;top:945px;width:1028px;height:255px;background:var(--footer)}
.footer-nav{left:198px;top:974px;list-style:none}
.footer-nav li{font-size:12px;color:var(--white);height:23px}
.footer-col h4{font-size:12px;font-weight:400;color:var(--white);margin-bottom:10px}
.footer-col p{font-size:8px;line-height:10.5px;color:#e6e6e6;margin-bottom:10px}
.footer-col a{color:var(--white);font-weight:700;text-decoration:underline}
.footer-rule{left:629px;top:1049px;width:202px;height:1px;background:#3a3a3a}
.footer-base{left:0;top:1163px;width:1028px;height:37px;background:var(--footer-base)}
.copyright{left:0;top:1177px;width:1028px;text-align:center;font-size:8px;color:#ccc}
</style>
</head>
<body>
<div class="abs top-rule"></div>

<header>
  <div class="abs brand">
    <span class="brand-dot"></span>
    <span class="brand-name">Koru Flow Septic Services</span>
  </div>
  <div class="abs divider" style="left:482px"></div>
  <p class="abs tagline">Our Septic tank maintenance services will help your septic system perform at optimum efficiency</p>
  <div class="abs divider" style="left:675px"></div>
  <p class="abs service-area">For Septic Tank servicing, installation and parts Auckland Wide</p>
  <svg class="abs phone-icon" width="25" height="25" viewBox="0 0 25 25" aria-hidden="true">
    <circle cx="12.5" cy="12.5" r="11" fill="none" stroke="#1dbb94" stroke-width="1.5"/>
    <path d="M9 7c1 0 2 2.5 2 3s-1 1-1 1.5 2 3.5 3.5 3.5c.5 0 1-1 1.5-1s3 1 3 2-1.5 2-2.5 2C11 18 7 13 7 9c0-1 1-2 2-2z" fill="#1dbb94"/>
  </svg>
  <p class="abs phones">09 555 0142<br>021 555 01 486</p>
</header>

<nav class="abs main-nav">
  <a class="is-active" style="left:5px">Home</a>
  <a style="left:48px">About us</a>
  <a style="left:110px">Deciphering your septic tank</a>
  <a style="left:287px">Servicing &amp; Maintenance</a>
  <a style="left:445px">Parts</a>
  <a style="left:491px">Free Quote</a>
  <a style="left:565px">Contact us</a>
</nav>

<section>
  <div class="abs hero" role="img" aria-label="Mountain river cascading over rocks beneath pine-covered slopes"></div>
  <svg class="abs" style="left:586px;top:138px" width="230" height="175" viewBox="0 0 230 175" aria-hidden="true">
    <path d="M4 0H226Q230 0 230 4V122Q200 140 140 145L110 172L108 145Q40 140 0 122V4Q0 0 4 0Z" fill="#fff" fill-opacity=".86"/>
  </svg>
  <div class="abs hero-callout">
    <h1>Want to learn more about how your septic tank works?</h1>
    <p>Koru Flow Septic Services are Auckland's best septic tank experts and will tell you everything there is to know.</p>
  </div>
  <div class="abs slider-dots">
    <span style="left:16px"></span><span style="left:26px"></span><span class="is-current" style="left:36px"></span><span style="left:46px"></span><span style="left:57px"></span>
  </div>
</section>

<section>
  <h2 class="abs intro-title">SED UT PERSPICIATIS UNDE OMNIS ISTE NA TUS ERROR ATS DFGIHI</h2>
  <p class="abs intro-sub">Lorem ipsum dolor sit amet, consectetur adipiscing elit, sed do eiusmod tempor.</p>
  <div class="abs intro-shadow"></div>
</section>

<section>
  <article class="abs feature" style="left:195px;top:485px">
    <h2>Looking for septic tanks parts in Auckland asap?</h2>
    <div class="photo" style="left:-3px;background:linear-gradient(160deg,#c9c2b4,#8b7a5e 60%,#5a4a36)" role="img" aria-label="New septic tank being lowered into an excavated hole"></div>
    <p style="left:2px;width:196px">If you need r<a>eplacement parts for septic tanks,</a> call us today! Koru Flow Septic Services will either have or can source the part you need fast and offer <a>septic tank part installation services</a> to ensure your parts are fitted correctly and work at optimum efficiency for longer. And often we can offer same day service when you're in a bind.</p>
    <span class="btn" style="left:1px;top:243px">More info</span>
  </article>
  <article class="abs feature" style="left:411px;top:485px">
    <h2>Want to know how to take care of your septic tank?</h2>
    <div class="photo" style="left:6px;background:linear-gradient(160deg,#6f8a48,#8c9a5a 50%,#5b6b34)" role="img" aria-label="Technician pumping out a septic tank on a lawn"></div>
    <p style="left:5px;width:200px">Most people when they buy a new property with a septic tank don't understand how their system works, or even what system they have! Koru Flow Septic Services will come inspect your septic tank anywhere in Auckland and offer DIY maintenance advice to avoid any messy or unnecessary problems with your septic tank.</p>
    <span class="btn" style="left:4px;top:242px">More info</span>
  </article>
  <article class="abs feature" style="left:633px;top:485px">
    <h2>When was the last time you serviced your septic tank?</h2>
    <div class="photo" style="left:3px;background:linear-gradient(160deg,#8c6e52,#c9c4bc 50%,#7a5a40)" role="img" aria-label="White polymer septic tank sitting in an open trench"></div>
    <p style="left:2px;width:198px">Standard septic tanks need to be serviced every 3 - 5 years and as each septic system has its own unique characteristics, such as internal parts and control panels. It can be difficult to service it thoroughly yourself. Koru Flow Septic Services have the experience, supplies and materials to service all septic tank systems, as well as helping you to <a>understand your septic tank system</a>.</p>
    <span class="btn" style="left:2px;top:243px">More info</span>
  </article>
  <p class="abs note"><b>Free Quote form</b> - similar to below but change to right colours and timeframe to 'contact you within four hours'.</p>
</section>

<section>
  <div class="abs enquiry"></div>
  <svg class="abs" style="left:195px;top:801px" width="212" height="105" viewBox="0 0 212 105" aria-hidden="true">
    <defs><linearGradient id="leadShade" x1="0" y1="0" x2="0" y2="1"><stop offset="0" stop-color="#2e2e2e"/><stop offset="1" stop-color="#3c3c3c"/></linearGradient></defs>
    <path d="M3 0H168L210 52L168 105H3Q0 105 0 102V3Q0 0 3 0Z" fill="url(#leadShade)"/>
  </svg>
  <div class="abs enquiry-lead">
    <h3>Make an Enquiry</h3>
    <p>fill out the form below and we will contac you within 24hrs.</p>
  </div>
  <div class="field" style="left:421px;top:811px;width:203px;height:18px">Name:</div>
  <div class="field" style="left:421px;top:834px;width:203px;height:18px">Email:</div>
  <div class="field" style="left:421px;top:858px;width:203px;height:18px">Contact Phone:</div>
  <div class="field" style="left:637px;top:810px;width:183px;height:65px">Details:</div>
  <div class="abs send">SEND</div>
</section>

<footer>
  <div class="abs site-footer"></div>
  <ul class="abs footer-nav">
    <li>&raquo;&nbsp; Home</li>
    <li>&raquo;&nbsp; About</li>
    <li>&raquo;&nbsp; Deciphering Your Septic tank</li>
    <li>&raquo;&nbsp; Servicing &amp; Maintenance</li>
    <li>&raquo;&nbsp; Parts</li>
    <li>&raquo; Free Quote</li>
    <li>&raquo; Contact</li>
  </ul>
  <div class="abs footer-col" style="left:414px;top:975px;width:170px">
    <h4>Company guarantee to you...</h4>
    <p>Koru Flow Septic Services travel throughout the Auckland region. Owner Rewi promises they will go through your system with a fine tooth comb and provide a comprehensive service.</p>
    <p>Koru Flow Septic Services aim to give clients more than they expect from their septic tank service.</p>
    <p>And most <a>septic tank parts</a> we sell come with a one year guarantee.</p>
  </div>
  <div class="abs footer-col" style="left:629px;top:975px;width:205px">
    <h4>Need your septic tank cleaned?</h4>
    <p>- Talk to the team at <a>Harlow Tank Cleaning Services</a>!</p>
  </div>
  <div class="abs footer-rule"></div>
  <div class="abs footer-col" style="left:629px;top:1090px;width:205px">
    <h4 style="margin-bottom:4px">For all polymer fabricated products</h4>
    <p>- Talk to the team at <a>Polyform 21 Limited</a>!</p>
  </div>
  <div class="abs footer-base"></div>
  <p class="abs copyright">&copy; 2014 KoruFlowServices. All Rights Reserved. Terms &amp; Conditions &nbsp;|&nbsp;Privacy Policy.</p>
</footer>
</body>
</html>
```